Corvane

I'm looking for business cards with the logo I've attached. I don't have an specific idea in mind and open to anything. All the usual info will be involved. Name, position in company, nr, email, address

```html
<!DOCTYPE html>
<html lang="en">
<head>
<meta charset="UTF-8">
<title>Corvane Designs – Business Cards</title>
<link rel="stylesheet" href="https://fonts.googleapis.com/css2?family=Montserrat:wght@500;700&family=Arimo:wght@400&display=swap">
<style>
  :root {
    --backdrop: #e9e8e6;
    --navy: #0b2a4a;
    --navy-deep: #082340;
    --navy-soft: #163a61;
    --gold: #e0a42c;
    --gold-edge: #c9962a;
    --ink-light: #e8ecf2;
    --rule: #9fb0c4;
  }
  * { margin: 0; padding: 0; box-sizing: border-box; }
  html, body {
    width: 1200px; height: 801px; overflow: hidden;
    background: var(--backdrop);
  }
  .stage {
    width: 1200px; height: 801px;
    display: flex; align-items: center; justify-content: center; gap: 48px;
  }
  .card {
    position: relative;
    width: 540px; height: 309px;
    background: linear-gradient(150deg, var(--navy-soft) 0%, var(--navy) 45%, var(--navy-deep) 100%);
    border-bottom: 3px solid var(--gold-edge);
    border-right: 2px solid var(--gold-edge);
    box-shadow: 0 14px 30px rgba(0,0,0,0.22);
    overflow: hidden;
  }

  /* Front */
  .brand {
    position: absolute; left: 0; right: 0; top: 58px;
    text-align: center;
    font-family: "Montserrat", sans-serif; font-weight: 700;
    color: var(--gold);
  }
  .brand__name { font-size: 44px; letter-spacing: 2px; line-height: 1; }
  .brand__sub { font-size: 15px; letter-spacing: 14px; margin-top: 8px; padding-left: 14px; }

  .details {
    position: absolute; left: 40px; right: 30px; top: 160px;
    display: flex; align-items: center;
  }
  .person { width: 200px; text-align: right; padding-right: 20px; }
  .person__name {
    font-family: "Montserrat", sans-serif; font-weight: 700;
    font-size: 19px; color: var(--gold); letter-spacing: 0.5px;
  }
  .person__role {
    font-family: "Arimo", sans-serif; font-size: 15px; color: var(--ink-light); margin-top: 3px;
  }
  .divider { width: 1px; height: 72px; background: var(--rule); }
  .contacts { list-style: none; padding-left: 20px; }
  .contacts li {
    display: flex; align-items: center; gap: 9px;
    font-family: "Arimo", sans-serif; font-size: 15px; color: var(--ink-light);
    line-height: 24px;
  }
  .contacts svg { width: 14px; height: 14px; flex: none; }

  .address {
    position: absolute; left: 0; right: 0; bottom: 34px;
    text-align: center;
    font-family: "Arimo", sans-serif; font-size: 15px; color: var(--ink-light);
  }

  /* Back */
  .card--back .brand { top: 116px; }
  .card--back .brand__name { font-size: 52px; }
</style>
</head>
<body>
<main class="stage">
  <section class="card card--front" aria-label="Business card front">
    <div class="brand">
      <div class="brand__name">CORVANE</div>
      <div class="brand__sub">DESIGNS</div>
    </div>

    <div class="details">
      <div class="person">
        <div class="person__name">ELIAS MARROW</div>
        <div class="person__role">Manager</div>
      </div>
      <div class="divider"></div>
      <ul class="contacts">
        <li>
          <svg viewBox="0 0 14 14" aria-hidden="true"><circle cx="7" cy="7" r="7" fill="var(--gold)"/><path d="M4.3 3.6c.4-.3.8-.2 1 .2l.6 1.2c.1.3 0 .6-.2.8l-.4.3c.4.9 1.1 1.6 2 2l.3-.4c.2-.2.5-.3.8-.2l1.2.6c.4.2.5.6.2 1-.5.8-1.4 1.1-2.3.6C6 8.9 5 7.9 4.3 6.5c-.5-1-.8-2.2 0-2.9z" fill="var(--navy)"/></svg>
          123-456-2100
        </li>
        <li>
          <svg viewBox="0 0 14 14" aria-hidden="true"><rect x="0.5" y="2.5" width="13" height="9" rx="1" fill="var(--gold)"/><path d="M1 3.2 7 8l6-4.8" stroke="var(--navy)" stroke-width="1.2" fill="none"/></svg>
          youremail@mailbox.com
        </li>
        <li>
          <svg viewBox="0 0 14 14" aria-hidden="true"><circle cx="7" cy="7" r="6.5" fill="var(--gold)"/><g stroke="var(--navy)" stroke-width="0.9" fill="none"><circle cx="7" cy="7" r="4.5"/><ellipse cx="7" cy="7" rx="2" ry="4.5"/><path d="M2.5 7h9"/></g></svg>
          www.yourwebsite.com
        </li>
      </ul>
    </div>

    <div class="address">Your address, city, state, ZIP 0000</div>
  </section>

  <section class="card card--back" aria-label="Business card back">
    <div class="brand">
      <div class="brand__name">CORVANE</div>
      <div class="brand__sub">DESIGNS</div>
    </div>
  </section>
</main>
</body>
</html>
```